Brochure Design Project

We need a brochure designed for our company, specifically targeted at our corporate business customers ... Banks, Financial Services, Government. The brochure needs to detail our services and what we have to offer.

It may be a brochure/booklet that we can give to clients when we meet them. It needs to have a very corporate look and feel and needs to align with our colour palette and logo.

Information is held on our website www.veltrexworldservices.com

Thank you everyone for being part of this project.  It was a very hard decision.

Target Market(s)

Corporate business and clients including banks, financial services, insurance and government.

Industry/Entity Type

Business

Requirements
Must have
• Must have a corporate and global feel to it.
Must have our logo and same or similar colour palette.

```html
<!DOCTYPE html>
<html lang="en">
<head>
<meta charset="utf-8">
<title>Veltrex World Services – Solutions Spread</title>
<link href="https://fonts.googleapis.com/css2?family=Source+Sans+3:wght@200;300;400;700;800&display=swap" rel="stylesheet">
<style>
  :root {
    --backdrop: #262626;
    --page-light: #f4f4f4;
    --page-band: #d9d9d9;
    --page-edge: #8f8f8f;
    --navy: #16195e;
    --ink: #1a1a1a;
    --muted: #9a9a9a;
    --title-grey: #a8a8a8;
    --dark-page: #141414;
    --photo-teal: #1f4a4f;
    --white-soft: #e6e6e6;
  }
  * { margin: 0; padding: 0; box-sizing: border-box; }
  html, body { width: 1200px; height: 793px; overflow: hidden; }
  body {
    background: var(--backdrop);
    font-family: "Source Sans 3", "Myriad Pro", sans-serif;
    position: relative;
  }
  .spread {
    position: absolute; left: 136px; top: 136px;
    width: 977px; height: 490px;
    display: flex;
  }
  .page { position: relative; height: 100%; }
  .page--left {
    width: 489px;
    background: linear-gradient(90deg, #ffffff 0%, var(--page-light) 70%, #e2e2e2 100%);
    overflow: hidden;
  }
  .page-header {
    position: absolute; left: 0; top: 0; width: 100%; height: 59px;
    background: linear-gradient(90deg, #e4e4e4, var(--page-band));
  }
  .page-title {
    position: absolute; left: 34px; top: 6px;
    font-weight: 200; font-size: 49px; letter-spacing: 1px;
    color: var(--title-grey); line-height: 1;
  }
  .page-footer {
    position: absolute; left: 0; bottom: 0; width: 100%; height: 6px;
    background: var(--page-edge);
  }
  .col { position: absolute; top: 70px; }
  .col--main { left: 35px; width: 202px; }
  .col--side { left: 273px; width: 195px; top: 72px; }
  .sector-title {
    font-weight: 800; font-size: 23px; line-height: 1.02;
    color: var(--navy); margin-bottom: 8px;
  }
  .lead { font-size: 10px; line-height: 1.3; color: var(--ink); margin-bottom: 9px; }
  .body-copy { font-size: 8px; line-height: 1.33; color: #333; }
  .body-copy p { margin-bottom: 9px; }
  .body-copy h3 {
    font-size: 8.5px; font-weight: 700; text-decoration: underline;
    margin: 4px 0 9px; color: var(--ink);
  }
  .list { list-style: none; margin-bottom: 9px; }
  .side-heading { font-size: 11.5px; font-weight: 800; color: var(--ink); margin-bottom: 8px; }
  .side-copy { font-size: 6.4px; line-height: 1.4; color: var(--muted); }
  .side-copy p { margin-bottom: 7px; }
  .side-copy .list { margin-bottom: 10px; }
  .section { margin-bottom: 10px; }

  .page--right { width: 488px; background: var(--dark-page); overflow: hidden; }
  .hero-photo {
    position: absolute; inset: 0;
    background:
      radial-gradient(ellipse 45% 40% at 52% 48%, rgba(60,170,170,0.45), transparent 70%),
      radial-gradient(ellipse 40% 60% at 45% 30%, #3a3532, transparent 75%),
      linear-gradient(180deg, #1b1b1b 0%, #101010 100%);
  }
  .site-url {
    position: absolute; right: 40px; top: 52px;
    font-size: 8.5px; color: #8a8a8a;
  }
  .hero-caption { position: absolute; left: 146px; top: 397px; width: 330px; color: var(--white-soft); }
  .hero-caption .headline { font-size: 11.5px; font-weight: 300; line-height: 1.3; margin-bottom: 10px; }
  .hero-caption .support { font-size: 8.3px; line-height: 1.35; color: #cfcfcf; }
</style>
</head>
<body>
  <main class="spread">
    <section class="page page--left">
      <div class="page-header"></div>
      <h1 class="page-title">SOLUTIONS</h1>

      <div class="col col--main">
        <h2 class="sector-title">Business,<br>Banking &amp; Finance</h2>
        <p class="lead">Our specialist team has extensive experience across all areas within Banking &amp; Financial Services</p>
        <div class="body-copy">
          <p>Whether you are optimising or transforming an existing business or creating something totally new we can assist.<br>Many of our models and systems have been designed specifically for this industry. They support all elements of business including</p>
          <ul class="list">
            <li>- Increasing customer satisfaction</li>
            <li>- Enhancing employee satisfaction</li>
            <li>- Improving revenue</li>
            <li>- Reducing cost</li>
          </ul>
          <h3>Our approach to solutions is based on</h3>
          <ul class="list">
            <li>- A multi-dimensional view of the business</li>
            <li>- Understanding the “whole” system to ensure all - impacts are managed</li>
            <li>- The belief that everything is connected and therefore ALL need to be accounted for within the change</li>
            <li>- Ensuring the People and Customer element is understood and supported throughout the transition.</li>
          </ul>
          <h3>We are different because</h3>
          <ul class="list">
            <li>- We specialise in working with ambiguity and complexity</li>
            <li>- We challenge current thinking and paradigms</li>
            <li>- We remove complexity, we don’t add to it</li>
            <li>- We understand how it works today to create how it works tomorrow</li>
            <li>- We monitor and measure the sustainability of the solution</li>
          </ul>
        </div>
      </div>

      <div class="col col--side">
        <div class="section">
          <h2 class="side-heading">Community</h2>
          <div class="side-copy">
            <p>There are many issues that impact all areas of our community. These issues have many causes which in turn can impact many other areas of the community such as:-</p>
            <ul class="list">
              <li>- Homelessness</li>
              <li>- Mental Health</li>
              <li>- Judicial System</li>
              <li>- Welfare System</li>
              <li>- Elderly Community</li>
              <li>- Indigenous Community</li>
              <li>- Juveniles and many others</li>
            </ul>
          </div>
        </div>
        <div class="section">
          <h2 class="side-heading">Environment</h2>
          <div class="side-copy">
            <p>There are many issues that impact all areas of our Environment. To create sustainable solutions all aspects of the Environmental system need to be understood and managed as a ‘whole’ system.</p>
            <p>Veltrex World Services specialise in working with complex problems that are multi-layered and have multiple interdependencies.</p>
            <p>Our approach to problem solving is holistic ensuring that the ‘whole’ system is understood and managed. We have found that if you impact one thing, you impact everything; therefore sustainable solutions for the Environment must encompass all aspects of the environment.</p>
          </div>
        </div>
        <div class="section">
          <h2 class="side-heading">Global</h2>
          <div class="side-copy">
            <p>There are many issues that impact all areas of our Global community.</p>
            <p>To create sustainable solutions all aspects of the Global system need to be understood and managed as a ‘whole’ system.</p>
            <p>Veltrex World Services specialise in working with complex problems that are multi-layered and have multiple interdependencies.</p>
            <p>Our approach to problem solving is holistic ensuring that the ‘whole’ system is understood and managed. We have found that if you impact one thing, you impact everything; therefore sustainable solutions for our Global Community must encompass all aspects of the community.</p>
          </div>
        </div>
      </div>
      <div class="page-footer"></div>
    </section>

    <section class="page page--right">
      <div class="hero-photo" role="img" aria-label="Photograph of a businessman in a dark suit holding a glowing holographic world map and data interface above his open hand"></div>
      <p class="site-url">www.veltrexworldservices.com</p>
      <div class="hero-caption">
        <p class="headline">Veltrex World Services specialise in working with complex problems that are multi-layered and have multiple interdependencies.</p>
        <p class="support">Our approach to problem solving is holistic ensuring that the ‘whole’ system is understood and managed. We have found that if you impact one thing, you impact everything; therefore sustainable solutions must encompass all aspects.</p>
      </div>
    </section>
  </main>
</body>
</html>
```